New Business Card Fairway Nine and MRCC

Create a business card for golf instructor

Target Market(s)

Golf

Contact Information for Business Card

I teach golf at my indoor facility (Fairway Nine Golf) and I teach at a nearby golf course (Maple Ridge Country Club) I am the Director of Instruction at both. I would like to see designs that include both my logo and the golf course logo.
Dennis Wrayburn, TSL
Director of Instruction
Fairway Nine Golf Inc.
4362 Orchard Vale Rd
Suite F
Cincinnati, OH 45871
My business slogan: Swing is Good. Fairway Nine is Better. Go Further
www.fairwaynine-example.com
e: info@fairwaynine-example.com
p: 513-555-0187

Font styles to use
Sans Serif

Requirements
Nice to have
• Red, White, Black, Grey Colors

```html
<!DOCTYPE html>
<html lang="en">
<head>
<meta charset="utf-8">
<title>Fairway Nine Golf & Maple Ridge Country Club Business Card</title>
<link href="https://fonts.googleapis.com/css2?family=Roboto:wght@400;500;700&display=swap" rel="stylesheet">
<style>
  :root {
    --bg: #e9e9e9;
    --card: #ffffff;
    --red: #e53a33;
    --red-soft: #ef7d78;
    --green: #1f6b2d;
    --green-light: #2f8a3f;
  }
  * { margin: 0; padding: 0; box-sizing: border-box; }
  html, body {
    width: 1200px; height: 801px; overflow: hidden;
    background: var(--bg);
    font-family: 'Roboto', Arial, sans-serif;
  }
  .stage {
    width: 1200px; height: 801px;
    display: flex; align-items: center; justify-content: center; gap: 40px;
  }
  .card {
    width: 560px; height: 320px;
    background: var(--card);
    border-bottom: 5px solid var(--red);
    box-shadow: 0 10px 30px rgba(0,0,0,0.15);
    position: relative;
    overflow: hidden;
  }
  /* Front card */
  .card--front { display: flex; align-items: center; }
  .brand {
    width: 260px; display: flex; align-items: center; justify-content: center; gap: 10px;
  }
  .brand__mark {
    width: 18px; height: 18px; background: var(--red); flex-shrink: 0;
  }
  .brand__name {
    color: var(--red); font-weight: 700; font-size: 24px; white-space: nowrap;
  }
  .divider {
    width: 1px; height: 150px; background: var(--red-soft); flex-shrink: 0;
  }
  .contact {
    padding-left: 30px; padding-right: 20px; color: var(--red);
  }
  .contact__name { font-size: 22px; font-weight: 700; white-space: nowrap; }
  .contact__role { font-size: 16px; color: var(--red-soft); margin-bottom: 12px; white-space: nowrap; }
  .contact__address { font-size: 13px; color: var(--red-soft); line-height: 1.4; margin-bottom: 12px; }
  .contact__list { list-style: none; font-size: 13px; line-height: 1.7; }
  .contact__list li { display: flex; align-items: center; gap: 8px; white-space: nowrap; }
  .contact__list svg { width: 12px; height: 12px; fill: var(--red); flex-shrink: 0; }
  /* Back card */
  .card--back {
    display: flex; flex-direction: column; align-items: center; justify-content: center; gap: 34px;
  }
  .club { display: flex; align-items: center; gap: 12px; }
  .club__mark { width: 22px; height: 22px; background: var(--green-light); flex-shrink: 0; }
  .club__name {
    color: var(--green); font-weight: 500; font-size: 26px; letter-spacing: 1px; white-space: nowrap;
  }
  .tagline { color: var(--green-light); font-size: 16px; white-space: nowrap; }
</style>
</head>
<body>
<main class="stage">
  <section class="card card--front">
    <div class="brand">
      <div class="brand__mark"></div>
      <div class="brand__name">Fairway Nine Golf</div>
    </div>
    <div class="divider"></div>
    <div class="contact">
      <div class="contact__name">Dennis Wrayburn, TSL</div>
      <div class="contact__role">Director of Instruction</div>
      <div class="contact__address">4362 Orchard Vale Rd<br>Suite F, Cincinnati, OH 45871</div>
      <ul class="contact__list">
        <li><svg viewBox="0 0 24 24"><path d="M6.6 10.8a15 15 0 0 0 6.6 6.6l2.2-2.2c.3-.3.7-.4 1-.2 1.1.4 2.3.6 3.6.6.6 0 1 .4 1 1V20c0 .6-.4 1-1 1A17 17 0 0 1 3 4c0-.6.4-1 1-1h3.5c.6 0 1 .4 1 1 0 1.3.2 2.5.6 3.6.1.3 0 .7-.2 1z"/></svg>513-555-0187</li>
        <li><svg viewBox="0 0 24 24"><path d="M2 5h20v14H2zm2 2v.5l8 5 8-5V7zm0 3v7h16v-7l-8 5z"/></svg>info@fairwaynine-example.com</li>
        <li><svg viewBox="0 0 24 24"><circle cx="12" cy="12" r="10"/></svg>www.fairwaynine-example.com</li>
      </ul>
    </div>
  </section>

  <section class="card card--back">
    <div class="club">
      <div class="club__mark"></div>
      <div class="club__name">Maple Ridge Country Club</div>
    </div>
    <p class="tagline">Swing is Good. Fairway Nine is Better. Go Further</p>
  </section>
</main>
</body>
</html>
```